Consumer Product Goods (Food) website

We need a simple, but clean and modern website for our new food branded company called Lantern Bay Foods.

Need a website that company can easily update. I added company logo and some images of our products. I added 1 package design of our products that's available now in the retail stores.

Company currently has 1 item but will be adding up to 5 items witin a few months. So need a website we can easily add new products.

Reason: We're guaranteeing payment and wanted to give more time for others to submit.

Target Market(s)

Customers that are seeking new adventurous novelty Asian foods.

Industry/Entity Type

Retail

Coding

Coded - Design and coding required

Number of Pages Required

3 page

Requirements
Must have
• I would like to have 3 pages: Homepage, Products Page, and Contact Us.
Nice to have
• I would like a nice visually clean and modern looking homepage. As you can see from the package design, it has a dark tone, so if we can try to make the website a dark blackgroup. I uploaded the dark background we used in our package. Maybe have the 3 different dumplings rotating images on the homepage.
• Products Page should have just 1 product right now; Kimchi & Pork dumplings. Maybe have like pic of the package design and have space for a briefly summary of product, ingredient list and nutrition fact. Should be a page where i can add more products to this page.
• Contact Us page can simply have map, email addres, and phone #.
• would be nice to have where the website is responsive to PC, tablet, and mobile phones

```html
<!DOCTYPE html>
<html lang="en">
<head>
<meta charset="utf-8">
<title>Lantern Bay Foods — Home</title>
<link href="https://fonts.googleapis.com/css2?family=Montserrat:wght@400;500;600&family=Tinos&display=swap" rel="stylesheet">
<style>
  :root {
    --bg-top: #1c1816;
    --bg-bottom: #0e0c0b;
    --white: #ffffff;
    --ink: #1a1a1a;
    --orange: #c9502f;
    --green: #8cc63f;
    --panel: rgba(112, 112, 112, 0.6);
    --rule: rgba(255, 255, 255, 0.22);
    --plate-light: #d8cfb4;
    --plate-dark: #2a2a2a;
  }
  * { margin: 0; padding: 0; box-sizing: border-box; }
  html, body { width: 1200px; height: 900px; overflow: hidden; }
  body {
    position: relative;
    font-family: "Montserrat", sans-serif;
    color: var(--white);
    background: radial-gradient(ellipse at 50% 40%, var(--bg-top), var(--bg-bottom) 80%);
  }
  .contact-item { position: absolute; top: 36px; display: flex; gap: 10px; font-size: 10.5px; line-height: 15px; font-weight: 500; }
  .contact-item strong { font-weight: 600; display: block; }
  .contact-item svg { margin-top: 5px; }
  .contact-phone { left: 160px; }
  .contact-email { left: 273px; }
  .brand { position: absolute; left: 500px; top: 24px; width: 200px; text-align: center; }
  .brand-dot { width: 30px; height: 30px; border-radius: 50%; background: var(--green); margin: 0 auto 8px; }
  .brand-name { font-size: 12px; font-weight: 600; letter-spacing: 1px; text-transform: uppercase; }
  .main-nav { position: absolute; left: 758px; top: 26px; display: flex; border: 1px solid var(--white); }
  .main-nav a { display: block; height: 36px; line-height: 36px; padding: 0 15px; font-size: 10.5px; font-weight: 500; color: var(--white); text-decoration: none; border-left: 1px solid var(--white); }
  .main-nav a:first-child { border-left: 0; }
  .main-nav a.active { background: var(--white); color: var(--ink); }
  .hero-tag { position: absolute; left: 311px; top: 296px; width: 278px; height: 60px; background: var(--orange); font-size: 30px; font-weight: 500; line-height: 60px; text-align: center; }
  .hero-title { position: absolute; left: 214px; top: 364px; width: 375px; height: 104px; background: var(--green); font-family: "Tinos", serif; font-size: 58px; line-height: 104px; text-align: center; letter-spacing: 0.5px; }
  .hero-text { position: absolute; left: 161px; top: 478px; width: 428px; height: 74px; background: var(--panel); padding: 18px 16px 0; font-size: 12px; line-height: 20px; text-align: right; font-weight: 500; }
  .read-more { position: absolute; left: 499px; top: 570px; width: 90px; height: 38px; border: 2px solid var(--white); font-size: 10.5px; font-weight: 600; line-height: 34px; text-align: center; color: var(--white); text-decoration: none; }
  .hero-photo { position: absolute; left: 604px; top: 312px; width: 436px; height: 276px; border-radius: 50%; background: radial-gradient(ellipse at 55% 45%, var(--plate-light) 0%, #b49a74 35%, var(--plate-dark) 68%, transparent 72%); }
  .slider-arrow { position: absolute; top: 735px; width: 30px; height: 30px; border: 1px solid var(--white); display: flex; align-items: center; justify-content: center; }
  .slider-prev { left: 519px; }
  .slider-next { left: 651px; }
  .slider-dots { position: absolute; top: 745px; left: 573px; display: flex; gap: 12px; }
  .slider-dots span { width: 10px; height: 10px; border-radius: 50%; border: 1px solid var(--white); }
  .slider-dots span.current { background: var(--white); }
  .site-footer { position: absolute; left: 0; top: 862px; width: 1200px; height: 38px; border-top: 1px solid var(--rule); font-size: 10.5px; font-weight: 500; }
  .copyright { position: absolute; left: 161px; top: 13px; }
  .footer-links { position: absolute; right: 161px; top: 12px; display: flex; gap: 27px; }
  .footer-links a { color: var(--white); text-decoration: none; }
</style>
</head>
<body>
  <header>
    <div class="contact-item contact-phone">
      <svg width="12" height="12" viewBox="0 0 24 24"><path fill="#fff" d="M6.6 10.8c1.4 2.8 3.8 5.2 6.6 6.6l2.2-2.2c.3-.3.7-.4 1-.2 1.1.4 2.3.6 3.6.6.6 0 1 .4 1 1V20c0 .6-.4 1-1 1C10.6 21 3 13.4 3 4c0-.6.4-1 1-1h3.5c.6 0 1 .4 1 1 0 1.3.2 2.5.6 3.6.1.3 0 .7-.2 1z"/></svg>
      <div>Call On :<strong>555 014 2283</strong></div>
    </div>
    <div class="contact-item contact-email">
      <svg width="16" height="12" viewBox="0 0 16 12"><rect width="16" height="12" rx="1" fill="#fff"/><path d="M1 1l7 5 7-5" stroke="#1a1614" stroke-width="1.6" fill="none"/></svg>
      <div>Get In Touch:<strong>hello@lanternbayfoods.com</strong></div>
    </div>
    <div class="brand">
      <div class="brand-dot"></div>
      <div class="brand-name">Lantern Bay Foods</div>
    </div>
    <nav class="main-nav">
      <a href="#" class="active">HOME</a>
      <a href="#">PRODUCT</a>
      <a href="#">ABOUT</a>
      <a href="#">CONTACT</a>
    </nav>
  </header>

  <main>
    <div class="hero-tag">KIMCHI &amp; PORK</div>
    <h1 class="hero-title">DUMPLINGS</h1>
    <p class="hero-text">Inspired by the name of a famous trade route that connected East Asia and Western countries, Lantern Bay</p>
    <a href="#" class="read-more">READ MORE</a>
    <div class="hero-photo" role="img" aria-label="Plate of kimchi and pork dumplings with lettuce and red onion"></div>

    <div class="slider-arrow slider-prev"><svg width="10" height="12" viewBox="0 0 10 12"><path d="M7 1L2 6l5 5" stroke="#fff" stroke-width="2" fill="none"/></svg></div>
    <div class="slider-dots"><span class="current"></span><span></span><span></span></div>
    <div class="slider-arrow slider-next"><svg width="10" height="12" viewBox="0 0 10 12"><path d="M3 1l5 5-5 5" stroke="#fff" stroke-width="2" fill="none"/></svg></div>
  </main>

  <footer class="site-footer">
    <div class="copyright">Lantern Bay Food. © All Reserved 2016</div>
    <nav class="footer-links">
      <a href="#">Home Page</a>
      <a href="#">About Us</a>
      <a href="#">Contact Us</a>
    </nav>
  </footer>
</body>
</html>
```